logo for security & safety training, education consultants
Marlow Advisory Nest Pte Ltd
Professional
LTC (RET) LIM BOON KEAT ROBERT MBA
DIRECTOR
47 JALAN TEMBUSIRA SINGAPORE 528806
robert@marlownest-example.com
www.marlownest-example.com
Perhaps some iso logo and same award logo in dummies

```html
<!DOCTYPE html>
<html lang="en">
<head>
<meta charset="utf-8">
<title>Marlow Advisory Nest – Business Card</title>
<link href="https://fonts.googleapis.com/css2?family=Open+Sans:wght@400;600;800&display=swap" rel="stylesheet">
<style>
  :root {
    --backdrop: #e4e4e6;
    --card: #ffffff;
    --brand-blue: #2626e6;
    --brand-navy: #1b1f4d;
    --swoosh: #111111;
    --text-light: #ffffff;
    --text-muted: #6b6b78;
  }
  * { box-sizing: border-box; margin: 0; padding: 0; }
  html, body { width: 1200px; height: 987px; overflow: hidden; }
  body {
    background: var(--backdrop);
    font-family: "Open Sans", Arial, sans-serif;
    position: relative;
  }
  .card {
    position: absolute;
    left: 220px;
    width: 760px;
    height: 430px;
    background: var(--card);
    border-radius: 26px;
    overflow: hidden;
    box-shadow: 0 10px 30px rgba(0,0,0,0.18);
  }
  .card--back { top: 40px; }
  .card--front { top: 515px; }

  .back-mark {
    position: absolute;
    top: 140px; left: 0; right: 0;
    display: flex; align-items: center; justify-content: center; gap: 12px;
  }
  .mark-dot { width: 22px; height: 22px; border-radius: 50%; background: var(--brand-blue); }
  .brand-name { font-weight: 800; color: var(--brand-navy); letter-spacing: 1px; }
  .back-mark .brand-name { font-size: 40px; }
  .back-web {
    position: absolute; top: 262px; left: 0; right: 0;
    text-align: center; font-size: 17px; letter-spacing: 5px; color: var(--text-muted);
  }

  .front-art { position: absolute; inset: 0; }
  .front-mark {
    position: absolute; top: 48px; left: 50px;
    display: flex; align-items: center; gap: 10px;
  }
  .front-mark .brand-name { font-size: 44px; }
  .person { position: absolute; left: 50px; top: 268px; color: var(--text-light); }
  .person-name { font-size: 14px; font-weight: 600; letter-spacing: 0.3px; }
  .person-role { font-size: 11px; letter-spacing: 1px; margin-top: 3px; }

  .contacts {
    position: absolute; left: 505px; top: 288px; list-style: none;
    color: var(--text-light); font-size: 11.5px; line-height: 16px;
  }
  .contacts li { display: flex; align-items: center; gap: 8px; min-height: 16px; margin-bottom: 3px; }
  .contacts li.address { align-items: flex-start; }
  .icon {
    width: 16px; height: 16px; border-radius: 50%; background: var(--text-light);
    display: flex; align-items: center; justify-content: center; flex: none;
  }
  .icon svg { width: 10px; height: 10px; fill: var(--brand-blue); }
</style>
</head>
<body>

<section class="card card--back" aria-label="Card back">
  <div class="back-mark">
    <span class="mark-dot"></span>
    <span class="brand-name">MARLOW</span>
  </div>
  <p class="back-web">www.marlownest-example.com</p>
</section>

<section class="card card--front" aria-label="Card front">
  <svg class="front-art" viewBox="0 0 760 430" preserveAspectRatio="none" aria-hidden="true">
    <path d="M0,150 C220,188 470,270 760,232 L760,250 C470,288 220,200 0,172 Z" fill="var(--swoosh)"/>
    <path d="M0,182 C220,212 470,300 760,260 L760,430 L0,430 Z" fill="var(--brand-blue)"/>
  </svg>

  <div class="front-mark">
    <span class="mark-dot"></span>
    <span class="brand-name">MARLOW</span>
  </div>

  <div class="person">
    <p class="person-name">LTC (RET) LIM BOON KEAT ROBERT MBA</p>
    <p class="person-role">DIRECTOR</p>
  </div>

  <ul class="contacts">
    <li class="address"><span class="icon"><svg viewBox="0 0 10 10"><path d="M5 0a3.5 3.5 0 0 0-3.5 3.5C1.5 6 5 10 5 10s3.5-4 3.5-6.5A3.5 3.5 0 0 0 5 0zm0 5a1.5 1.5 0 1 1 0-3 1.5 1.5 0 0 1 0 3z"/></svg></span><span>47 JALAN TEMBUSIRA<br>SINGAPORE 528806</span></li>
    <li><span class="icon"><svg viewBox="0 0 10 10"><path d="M2 0.5l2 2-1 1.2c.6 1.3 1.6 2.3 2.9 2.9l1.2-1 2 2-1.2 1.6C4 9 1 6 0.6 1.8z"/></svg></span>+65 6140 2281</li>
    <li><span class="icon"><svg viewBox="0 0 10 10"><rect x="2.5" y="0.5" width="5" height="9" rx="1"/></svg></span>+65 9170 3346</li>
    <li><span class="icon"><svg viewBox="0 0 10 10"><rect x="1" y="3" width="8" height="5" rx="0.8"/><rect x="2.5" y="0.8" width="5" height="2.5"/></svg></span>+65 6158 0492</li>
    <li><span class="icon"><svg viewBox="0 0 10 10"><path d="M0.5 2h9v6h-9z M0.5 2l4.5 3.5L9.5 2" fill="none" stroke="#2626e6" stroke-width="1.2"/></svg></span>robert@marlownest-example.com</li>
    <li><span class="icon"><svg viewBox="0 0 10 10"><circle cx="5" cy="5" r="4" fill="none" stroke="#2626e6" stroke-width="1.1"/><path d="M1 5h8M5 1c-2 2.5-2 5.5 0 8M5 1c2 2.5 2 5.5 0 8" fill="none" stroke="#2626e6" stroke-width="0.9"/></svg></span>www.marlownest-example.com</li>
  </ul>
</section>

</body>
</html>
```